Coastal Gin Label Design

We are needing a nautical/coastal themed label for our upcoming gin release.

We have saltbush, cucumber, juniper, and quandong being used in this gin.

Name of the Gin; Harbor Glow

The logo attached is the company logo, but doesn't have to be used on the front of the label, ie it can just be the name Fernwhistle somewhere on the front.
Bottle specs attached as well so you can accurately represent the bottle- this bottle is also clear.

Target Market(s)

Women 25- 45

Font styles to use
Serif
Decorative

Colors
d5edf4
86cae7
33a6d7
86cfc6
cfeae6
ffffff
f6faec
ecf7fb
fefeff

Requirements
Must have
• Ocean/Coastal vibe to the label
Nice to have
• Blues,Whites clean and crisp
Should not have
• No generic word art look to it.
A dark mood

```html
<!DOCTYPE html>
<html lang="en">
<head>
<meta charset="UTF-8">
<title>Harbor Glow Gin — Label</title>
<link rel="stylesheet" href="https://fonts.googleapis.com/css2?family=Cinzel:wght@500&family=Bungee&family=Josefin+Sans:wght@600&family=Roboto+Condensed:wght@400&display=swap">
<style>
  :root {
    --backdrop: #f4f5f5;
    --label-white: #fefeff;
    --gold: #c9a94f;
    --gold-light: #dcc27a;
    --sea-deep: #0f8f86;
    --sea-mid: #1fae9f;
    --sea-light: #86cfc6;
    --foam: #ecf7fb;
    --sand: #e7d9b4;
    --text-white: #ffffff;
  }
  * { margin: 0; padding: 0; box-sizing: border-box; }
  html, body {
    width: 900px;
    height: 1200px;
    overflow: hidden;
    background: var(--backdrop);
  }
  .canvas {
    position: relative;
    width: 900px;
    height: 1200px;
  }
  .label {
    position: absolute;
    left: 70px;
    top: 10px;
    width: 760px;
    height: 1180px;
    background: var(--label-white);
    overflow: hidden;
    box-shadow: 0 2px 10px rgba(0,0,0,0.06);
  }
  .label__brand {
    position: absolute;
    top: 90px;
    width: 100%;
    text-align: center;
    font-family: 'Cinzel', serif;
    font-weight: 500;
    font-size: 54px;
    letter-spacing: 2px;
    color: var(--gold);
  }
  .label__name {
    position: absolute;
    top: 330px;
    width: 100%;
    text-align: center;
    font-family: 'Bungee', sans-serif;
    font-size: 128px;
    line-height: 1.02;
    color: var(--gold-light);
  }
  .label__sea {
    position: absolute;
    left: 0;
    top: 620px;
    width: 760px;
    height: 560px;
  }
  .label__type {
    position: absolute;
    top: 690px;
    width: 100%;
    text-align: center;
    font-family: 'Josefin Sans', sans-serif;
    font-weight: 600;
    font-size: 88px;
    letter-spacing: 10px;
    color: var(--text-white);
    text-shadow: 0 2px 6px rgba(0,0,0,0.45);
  }
  .label__rule {
    position: absolute;
    top: 1050px;
    left: 166px;
    width: 428px;
    height: 3px;
    background: var(--text-white);
  }
  .label__specs {
    position: absolute;
    top: 1072px;
    width: 100%;
    display: flex;
    justify-content: center;
    gap: 46px;
    font-family: 'Roboto Condensed', sans-serif;
    font-size: 33px;
    color: var(--text-white);
  }
</style>
</head>
<body>
<div class="canvas">
  <div class="label">
    <svg class="label__sea" viewBox="0 0 760 560" role="img" aria-label="Aerial photograph of turquoise ocean waves breaking over a sandy shore">
      <defs>
        <linearGradient id="sea-water" x1="1" y1="0" x2="0" y2="1">
          <stop offset="0" stop-color="#86cfc6"/>
          <stop offset="0.35" stop-color="#1fae9f"/>
          <stop offset="0.75" stop-color="#0f8f86"/>
          <stop offset="1" stop-color="#33a6b0"/>
        </linearGradient>
        <linearGradient id="sea-shore" x1="1" y1="0" x2="0" y2="1">
          <stop offset="0" stop-color="#fefeff" stop-opacity="0"/>
          <stop offset="0.3" stop-color="#e7d9b4"/>
          <stop offset="0.7" stop-color="#ecf7fb"/>
          <stop offset="1" stop-color="#d8cfa8"/>
        </linearGradient>
      </defs>
      <path d="M760 0 C 640 40 520 110 380 180 C 240 250 110 320 0 420 L 0 560 L 760 560 Z" fill="url(#sea-shore)"/>
      <path d="M760 60 C 650 110 540 170 420 230 C 290 300 150 380 0 470 L 0 560 L 760 560 Z" fill="url(#sea-water)"/>
    </svg>
    <div class="label__brand">FERNWHISTLE</div>
    <div class="label__name">HARBOR<br>GLOW</div>
    <div class="label__type">GIN</div>
    <div class="label__rule"></div>
    <div class="label__specs"><span>42% ALC/VOL</span><span>750ML</span></div>
  </div>
</div>
</body>
</html>
```